USA Home and Kitchen "Multi-Product" Brand Needs a Stunning Packaging Design.

We need a new packaging design for our Brand: T&M Hearth & Nest. We Manufacture, Market, and Sell Home & Kitchen Products (Such as Kitchen Utensils and Home Decor to name a few) Direct to Consumers in the United States via our Website and Vendora.com. We would like to see designs that are simple, clean, and modern, yet stand out and demand attention. Our Preferred colors of the design should include: Black or Grey as the base color/shade), White or Grey for the text, and some additional color can be used for complementary elements/visuals at your own discretion or creativity. We would like this to be an Interchangeable Design that can be easily modified and implemented across all of our other products (i.e: does not contain too many images or design elements that reference a particular product.

Although this design and the concept as a whole is intended to be used across our entire catalogue of products. Please feel free to base your design on our one of our top selling products as per the following URL: https://www.vendora-shop.example/dp/X93QL4471Z?ref=abc_item_dp.

Target Market(s)

Our customers tend come from many areas across the spectrum. But the quintessential T&M target customer (the type of person who tends to be our most receptive and loyal customer) is female and part of the Millennials generation, aged in her 30s, and is either working full-time in a white-collar job or on home duties, of which she would have young children, a spouse, or other family members to look after. She’s part of the conventional family life who represent the core of ‘middle America’. She doesn’t mind to splurge every now and again on shopping for items that she wants and/or needs, whilst some of the time she’ll also go out of her way to ‘search for a bargain’. She tends to spend more time in her home and kitchen than the average individual. We recognize that cooking for herself and family, and providing a well furnished and stylish home is part of who she is.

Industry/Entity Type

Retail

Font styles to use
Serif
Sans Serif

Colors

Designer to choose only greyscale colors for use in the design.

Requirements
Must have
• Interchangeable Design (A "Universal" Packaging Design that can be easily modified and adapted for use with a large catalogue of products under our brand).
Nice to have
• Some visual elements that gives our packaging/brand the ability to stand out and be unique/memorable.
Should not have
• Our design should not have too much text. Nor should it be cluttered or overcrowded with too much information or visual elements. And does not contain too many images or design elements that reference a particular product. We believe simplicity is key, and quality over quantity.

```html
<!DOCTYPE html>
<html lang="en">
<head>
<meta charset="utf-8">
<title>T&amp;M Hearth &amp; Nest — Pie Server Packaging</title>
<link href="https://fonts.googleapis.com/css2?family=Montserrat:wght@800&display=swap" rel="stylesheet">
<style>
  :root {
    --backdrop: #e2e2e2;
    --box-black: #0d0d0d;
    --side-black: #070707;
    --ink-white: #ffffff;
    --side-ink: #d9d9d9;
    --amber: #e0a03c;
    --amber-deep: #9c6c2a;
  }
  * { margin: 0; padding: 0; box-sizing: border-box; }
  html, body {
    width: 1200px; height: 789px; overflow: hidden;
    background: var(--backdrop);
    font-family: "Montserrat", Arial, sans-serif;
    font-weight: 800;
  }
  .dieline {
    position: absolute; left: 465px; top: 45px;
    display: flex; height: 700px;
  }
  .panel { position: relative; height: 100%; overflow: hidden; }
  .panel-side { width: 72px; background: var(--side-black); }
  .panel-front { width: 196px; background: var(--box-black); }

  .brand-name {
    position: absolute; left: 0; right: 0;
    text-align: center; color: var(--ink-white);
    white-space: nowrap; line-height: 1;
  }
  .panel-front .brand-name { top: 100px; font-size: 12px; letter-spacing: 0.02em; }
  .panel-side .brand-name { top: 70px; font-size: 5px; letter-spacing: 0.02em; color: var(--side-ink); }

  .product-title {
    position: absolute; left: 0; right: 0; top: 262px;
    text-align: center; color: var(--ink-white);
    font-size: 40px; line-height: 0.98; letter-spacing: -0.01em;
  }
  .product-tagline {
    position: absolute; left: 0; right: 0; top: 356px;
    text-align: center; color: var(--ink-white);
    font-size: 11.5px; letter-spacing: 0;
    white-space: nowrap;
  }

  .side-title {
    position: absolute; left: 50%; top: 330px;
    transform: translate(-50%, -50%) rotate(90deg);
    white-space: nowrap; text-align: center;
    color: var(--side-ink); font-size: 24px; line-height: 1;
  }

  .pattern-area {
    position: absolute; left: 0; right: 0; bottom: 0;
  }
  .panel-front .pattern-area {
    height: 250px;
    background: linear-gradient(180deg, rgba(224,160,60,0) 0%, rgba(224,160,60,0.55) 35%, var(--amber) 100%);
  }
  .panel-side .pattern-area {
    height: 130px;
    background: linear-gradient(180deg, rgba(156,108,42,0) 0%, var(--amber-deep) 100%);
  }
</style>
</head>
<body>
  <main class="dieline">
    <section class="panel panel-side">
      <p class="brand-name">T&amp;M Hearth &amp; Nest</p>
      <h2 class="side-title">PIE<br>SERVER</h2>
      <div class="pattern-area" role="img" aria-label="Amber honeycomb hexagon pattern"></div>
    </section>
    <section class="panel panel-front">
      <p class="brand-name">T&amp;M Hearth &amp; Nest</p>
      <h1 class="product-title">PIE<br>SERVER</h1>
      <p class="product-tagline">CUT AND SERVE SPATULA</p>
      <div class="pattern-area" role="img" aria-label="Amber honeycomb hexagon pattern rising from the base"></div>
    </section>
  </main>
</body>
</html>
```